KELPMARROW, LLC needs a hybrid app to evaluate and develop athletes

KELPMARROW, LLC needs initial hybrid mobile app and website holding page. KELPMARROW, LLC allows athletes to develop their skills (soccer is initial sport) for free. Receive daily/weekly reminders. Access training videos. Earn points to "upgrade" their soccer profile in "app soccer store". See their points/rankings compared to all app users. Progress streak. This free app (for athletes) will communicate to paid app (coaches) in the future. We would like to see designs use the color blue. The design will communicate health and wellness.

```html
<!DOCTYPE html>
<html lang="en">
<head>
<meta charset="utf-8">
<title>Kelpmarrow — Athlete App Screens</title>
<link href="https://fonts.googleapis.com/css2?family=Mulish:wght@400;500;600;700&display=swap" rel="stylesheet">
<style>
  :root {
    --page-bg: #f6f6f6;
    --screen-bg: #f5f7fa;
    --screen-edge: #e1e6ec;
    --brand-blue: #0457a6;
    --wave-light: #cddcec;
    --tab-bg: #d0dff0;
    --ink: #1e1e1e;
    --muted: #8a8f96;
    --rule: #d6dbe1;
    --icon-grey: #8b8f9c;
    --icon-soft: #7ea5d4;
  }
  * { box-sizing: border-box; margin: 0; padding: 0; }
  html, body {
    width: 750px; height: 1200px; overflow: hidden;
    background: var(--page-bg);
    font-family: "Mulish", "Helvetica Neue", Arial, sans-serif;
    color: var(--ink);
  }
  .canvas { position: relative; width: 750px; height: 1200px; }

  .screen {
    position: absolute;
    width: 360px; height: 640px;
    background: var(--screen-bg);
    border: 1px solid var(--screen-edge);
    overflow: hidden;
    transform: scale(.5);
    transform-origin: 0 0;
    box-shadow: 0 20px 40px rgba(0,0,0,.06);
  }
  .screen--login   { left: 160px; top: 206px; }
  .screen--signup  { left: 410px; top: 206px; }
  .screen--video   { left: 160px; top: 664px; }
  .screen--profile { left: 410px; top: 664px; }

  .abs { position: absolute; }
  .header-wave { position: absolute; left: 0; top: 0; width: 360px; height: 92px; }
  .footer-wave { position: absolute; left: 0; bottom: 0; width: 360px; height: 56px; }
  .brand {
    position: absolute; left: 0; right: 0; top: 16px;
    text-align: center; color: #fff;
    font-size: 17px; font-weight: 600; letter-spacing: .2px;
  }
  .screen-title {
    position: absolute; left: 0; right: 0; top: 114px;
    text-align: center; font-size: 21px; font-weight: 500; letter-spacing: .3px;
  }
  .field {
    position: absolute; left: 20px; width: 320px; height: 40px;
    border-bottom: 1px solid var(--rule);
    font-size: 15px; color: var(--muted);
    padding: 10px 0 0 19px;
  }
  .field .chevron { position: absolute; right: 20px; top: 16px; width: 14px; height: 8px; }
  .btn {
    position: absolute; left: 20px; width: 320px; height: 40px;
    display: flex; align-items: center; justify-content: center;
    font-size: 15px; font-weight: 700;
  }
  .btn--solid { background: var(--brand-blue); color: #fff; }
  .btn--outline { border: 2px solid var(--brand-blue); color: var(--brand-blue); font-weight: 600; }
  .note {
    position: absolute; left: 0; right: 0; text-align: center;
    font-size: 15px; color: var(--muted);
  }
  .note b { color: var(--brand-blue); font-weight: 700; font-size: 17px; }
  .rule { position: absolute; left: 20px; width: 320px; height: 1px; background: var(--rule); }

  .lesson-text { position: absolute; left: 170px; font-size: 15px; line-height: 22px; }
  .stat-line { position: absolute; left: 0; right: 0; text-align: center; font-size: 14px; }

  .tab-bar {
    position: absolute; left: 0; bottom: 0; width: 360px; height: 80px;
    background: var(--tab-bg);
  }
  .tab-bar svg { position: absolute; top: 24px; width: 34px; height: 34px; }

  .avatar-ring {
    position: absolute; left: 105px; top: 167px; width: 150px; height: 150px;
    border-radius: 50%; background: var(--screen-bg); border: 2px solid #dde3ea;
  }
  .avatar-photo {
    position: absolute; left: 9px; top: 9px; width: 128px; height: 128px; border-radius: 50%;
    background: radial-gradient(circle at 50% 70%, #e8ecf2 0 30%, #3a3632 31% 60%, #1f1d1b 100%);
  }
  .athlete-id { position: absolute; left: 0; right: 0; top: 334px; text-align: center; font-size: 16px; }
  .athlete-id span { color: var(--brand-blue); font-size: 17px; }
  .stats { position: absolute; left: 40px; top: 391px; font-size: 15px; line-height: 30px; }
  .stats .row { display: flex; }
  .stats .label { width: 145px; }
  .stats .colon { width: 35px; }
  .stats .value { color: var(--brand-blue); font-size: 14px; }
</style>
</head>
<body>
<div class="canvas">

  <svg width="0" height="0" style="position:absolute">
    <defs>
      <g id="header-wave-shape">
        <path d="M0 0H360V92C330 90 300 72 270 62C245 54 220 52 200 60C170 70 150 80 120 82C80 84 40 70 0 40Z" fill="#cddcec"/>
        <path d="M0 0H360V90C320 88 300 68 270 62C240 55 225 60 205 66C180 70 170 55 190 60C160 66 140 80 110 80C70 80 40 60 0 42Z" fill="#0457a6"/>
      </g>
    </defs>
  </svg>

  <!-- Login -->
  <section class="screen screen--login">
    <svg class="header-wave" viewBox="0 0 360 92" aria-hidden="true">
      <path d="M0 40C20 60 60 95 120 78C160 66 180 50 225 62C260 70 280 55 360 90V0H0Z" fill="#cddcec"/>
      <path d="M0 0H360V90C320 90 300 70 270 64C240 57 215 54 185 60C155 66 140 80 110 78C70 76 40 56 0 42Z" fill="#0457a6"/>
      <path d="M0 90C20 80 60 74 95 80L0 92Z" fill="#cddcec"/>
    </svg>
    <div class="brand">KELPMARROW</div>
    <h1 class="screen-title">ATHLETE LOGIN</h1>
    <div class="field" style="top:176px">Username:</div>
    <div class="field" style="top:246px">Password:</div>
    <div class="btn btn--solid" style="top:345px">Sign in</div>
    <div class="note" style="top:403px;padding-right:16px">Forgot Password?</div>
    <div class="rule" style="top:457px"></div>
    <div class="note" style="top:483px">Don't Have an Account?</div>
    <div class="btn btn--outline" style="top:519px">Create Account</div>
    <svg class="footer-wave" viewBox="0 0 360 56" aria-hidden="true">
      <path d="M0 10C40 -2 80 20 110 30C160 44 200 10 260 14C300 18 330 40 360 56H0Z" fill="#cddcec"/>
      <path d="M0 56C30 30 70 10 120 16C170 22 190 44 230 38C280 30 300 0 360 0V56Z" fill="#0457a6"/>
    </svg>
  </section>

  <!-- Create account -->
  <section class="screen screen--signup">
    <svg class="header-wave" viewBox="0 0 360 92" aria-hidden="true">
      <path d="M0 40C20 60 60 95 120 78C160 66 180 50 225 62C260 70 280 55 360 90V0H0Z" fill="#cddcec"/>
      <path d="M0 0H360V90C320 90 300 70 270 64C240 57 215 54 185 60C155 66 140 80 110 78C70 76 40 56 0 42Z" fill="#0457a6"/>
      <path d="M0 90C20 80 60 74 95 80L0 92Z" fill="#cddcec"/>
    </svg>
    <div class="brand">KELPMARROW</div>
    <h1 class="screen-title">CREATE ACCOUNT</h1>
    <div class="field" style="top:176px">Full Name:</div>
    <div class="field" style="top:246px">Age:</div>
    <div class="field" style="top:316px">Gender:
      <svg class="chevron" viewBox="0 0 14 8"><path d="M1 1L7 7L13 1" fill="none" stroke="#8a8f96" stroke-width="1.3"/></svg>
    </div>
    <div class="field" style="top:386px">Country:
      <svg class="chevron" viewBox="0 0 14 8"><path d="M1 1L7 7L13 1" fill="none" stroke="#8a8f96" stroke-width="1.3"/></svg>
    </div>
    <div class="field" style="top:456px">State/ZIP or Region:</div>
    <div class="btn btn--solid" style="top:536px">Submit</div>
    <div class="note" style="top:598px">Already Have an Account? <b>Sign in</b></div>
  </section>

  <!-- Training video -->
  <section class="screen screen--video">
    <svg class="header-wave" viewBox="0 0 360 92" aria-hidden="true">
      <path d="M0 40C20 60 60 95 120 78C160 66 180 50 225 62C260 70 280 55 360 90V0H0Z" fill="#cddcec"/>
      <path d="M0 0H360V90C320 90 300 70 270 64C240 57 215 54 185 60C155 66 140 80 110 78C70 76 40 56 0 42Z" fill="#0457a6"/>
      <path d="M0 90C20 80 60 74 95 80L0 92Z" fill="#cddcec"/>
    </svg>
    <div class="brand">KELPMARROW</div>
    <h1 class="screen-title" style="text-transform:none">Training Video</h1>
    <div class="rule" style="top:176px"></div>

    <svg class="abs" style="left:20px;top:196px" width="124" height="100" viewBox="0 0 124 100" aria-hidden="true">
      <g fill="none" stroke="#8b8f9c" stroke-width="2.5">
        <rect x="1.5" y="1.5" width="121" height="97"/>
        <line x1="1.5" y1="14" x2="122.5" y2="14"/>
        <rect x="21" y="26" width="82" height="58"/>
        <circle cx="62" cy="51" r="17"/>
        <path d="M56 42V60L70 51Z"/>
        <line x1="26" y1="73" x2="98" y2="73"/>
      </g>
      <g fill="#8b8f9c"><circle cx="94" cy="8" r="1.8"/><circle cx="102" cy="8" r="1.8"/><circle cx="110" cy="8" r="1.8"/><circle cx="44" cy="73" r="3"/></g>
    </svg>
    <p class="lesson-text" style="top:210px">Training Pillar<br>Length of Video Average<br>Touches, encourage x10</p>
    <div class="rule" style="top:326px"></div>

    <svg class="abs" style="left:25px;top:356px" width="114" height="102" viewBox="0 0 114 102" aria-hidden="true">
      <g fill="none" stroke="#8b8f9c" stroke-width="2.5">
        <rect x="1.5" y="22" width="110" height="78"/>
        <path d="M12 22V12H102V22M22 12V2H92V12"/>
        <path d="M44 44V78L72 61Z"/>
      </g>
    </svg>
    <p class="lesson-text" style="top:382px">Your Kelpmarrow<br>Video Library</p>
    <div class="rule" style="top:478px"></div>
    <p class="stat-line" style="top:487px;padding-right:24px">Accomplished 10 of 17 Weeks</p>
    <div class="rule" style="top:519px"></div>
    <p class="stat-line" style="top:529px">5 Weeks in A Row!</p>

    <nav class="tab-bar">
      <svg style="left:36px" viewBox="0 0 34 34"><g fill="none" stroke="#0457a6" stroke-width="2"><circle cx="17" cy="17" r="13"/><path d="M17 11L22.7 15.1 20.5 21.9H13.5L11.3 15.1Z"/><path d="M17 11V4M22.7 15.1L29 13M20.5 21.9L25 28M13.5 21.9L9 28M11.3 15.1L5 13"/></g></svg>
      <svg style="left:121px" viewBox="0 0 34 34"><g fill="none" stroke="#7ea5d4" stroke-width="2"><circle cx="17" cy="11" r="7"/><path d="M5 31C5 23 10 19 17 19S29 23 29 31"/></g></svg>
      <svg style="left:206px" viewBox="0 0 34 34"><path d="M17 3L29 7V16C29 24 23 29 17 32C11 29 5 24 5 16V7Z" fill="none" stroke="#7ea5d4" stroke-width="2"/></svg>
      <svg style="left:291px" viewBox="0 0 34 34"><g fill="none" stroke="#7ea5d4" stroke-width="2"><path d="M3 8L9 4L16 12C20 15 26 18 31 22L30 28L3 12Z"/><path d="M8 20L6 24M14 23L12 27M21 26L19 30M10 9L14 7M13 13L17 11"/></g></svg>
    </nav>
  </section>

  <!-- Profile -->
  <section class="screen screen--profile">
    <svg class="header-wave" viewBox="0 0 360 92" aria-hidden="true">
      <path d="M0 40C20 60 60 95 120 78C160 66 180 50 225 62C260 70 280 55 360 90V0H0Z" fill="#cddcec"/>
      <path d="M0 0H360V90C320 90 300 70 270 64C240 57 215 54 185 60C155 66 140 80 110 78C70 76 40 56 0 42Z" fill="#0457a6"/>
      <path d="M0 90C20 80 60 74 95 80L0 92Z" fill="#cddcec"/>
    </svg>
    <div class="brand">KELPMARROW</div>
    <h1 class="screen-title" style="text-transform:none">Profile</h1>
    <div class="rule" style="top:242px"></div>
    <div class="avatar-ring">
      <div class="avatar-photo" role="img" aria-label="Portrait photo of the athlete in a white team shirt"></div>
    </div>
    <p class="athlete-id"><span>#AZ12345</span> (Dario Penwick)</p>
    <div class="rule" style="top:371px"></div>
    <div class="stats">
      <div class="row"><span class="label">Primary Position</span><span class="colon">:</span><span class="value">7</span></div>
      <div class="row"><span class="label">Secondary Position :</span><span class="colon"></span><span class="value">5</span></div>
      <div class="row"><span class="label">Height</span><span class="colon">:</span><span class="value">5'6"</span></div>
      <div class="row"><span class="label">Weight</span><span class="colon">:</span><span class="value">148 ibs</span></div>
      <div class="row"><span class="label">Age</span><span class="colon">:</span><span class="value">18</span></div>
    </div>

    <nav class="tab-bar">
      <svg style="left:36px" viewBox="0 0 34 34"><g fill="none" stroke="#0457a6" stroke-width="2"><circle cx="17" cy="17" r="13"/><path d="M17 11L22.7 15.1 20.5 21.9H13.5L11.3 15.1Z"/><path d="M17 11V4M22.7 15.1L29 13M20.5 21.9L25 28M13.5 21.9L9 28M11.3 15.1L5 13"/></g></svg>
      <svg style="left:121px" viewBox="0 0 34 34"><g fill="none" stroke="#7ea5d4" stroke-width="2"><circle cx="17" cy="11" r="7"/><path d="M5 31C5 23 10 19 17 19S29 23 29 31"/></g></svg>
      <svg style="left:206px" viewBox="0 0 34 34"><path d="M17 3L29 7V16C29 24 23 29 17 32C11 29 5 24 5 16V7Z" fill="none" stroke="#7ea5d4" stroke-width="2"/></svg>
      <svg style="left:291px" viewBox="0 0 34 34"><g fill="none" stroke="#7ea5d4" stroke-width="2"><path d="M3 8L9 4L16 12C20 15 26 18 31 22L30 28L3 12Z"/><path d="M8 20L6 24M14 23L12 27M21 26L19 30M10 9L14 7M13 13L17 11"/></g></svg>
    </nav>
  </section>

</div>
</body>
</html>
```